Online Travel Agency card design with 2 logos

Need a two sided business card design for online tourism agency which is based in Istanbul Turkey.
Need a business card design where it shows the travel agency logo but also the logo and information of the parent company as well.Parent company logo is just text with 2 different colors. (Arial font with text TemaVista "Tema"- hex #172841 and "Vista" hex-#FF7F00)
Both logos are uploaded.
Target Market(s)
travel , online
Industry/Entity Type
Travel
Contact Information for Business Card
The information on the card should be as :
Travel Agency Logo logo (rnlogo)
Parent Company logo(temalogo)
Company information :TemaVista Turizm ve Bilgi Teknolojileri A.Ş
Address of company
Tel
Email
Name
Position(english and turkish)
Look and feel
Each slider illustrates characteristics of the customer's brand and the style your logo design should communicate.

```html
<!DOCTYPE html>
<html lang="tr">
<head>
<meta charset="utf-8">
<title>TemaVista – rahatrota Business Card</title>
<link rel="stylesheet" href="https://fonts.googleapis.com/css2?family=Open+Sans:wght@300;400;600;700;800&display=swap">
<style>
  :root {
    --navy: #172841;
    --sky: #6dd0e9;
    --sky-pale: #d3f0f8;
    --sky-mid: #a9e1f1;
    --white: #ffffff;
    --ink: #1b2a3f;
    --font: "Open Sans", Arial, sans-serif;
  }
  * { margin: 0; padding: 0; box-sizing: border-box; }
  html, body {
    width: 950px; height: 1200px; overflow: hidden;
    background: var(--white); font-family: var(--font);
  }
  .canvas { position: relative; width: 950px; height: 1200px; }

  .card { position: absolute; left: 0; width: 950px; overflow: hidden; }
  .card-front { top: 0; height: 537px; box-shadow: 0 10px 14px rgba(0,0,0,.28); }
  .card-back { top: 674px; height: 526px; background: var(--sky); }

  .card-shapes { position: absolute; inset: 0; }

  .brand-parent {
    position: absolute; font-weight: 400; color: var(--navy);
    letter-spacing: -0.5px; line-height: 1;
  }
  .brand-agency {
    position: absolute; display: flex; align-items: center; gap: 10px;
  }
  .brand-agency .mark {
    border-radius: 50%; background: var(--navy); flex: none;
  }
  .brand-agency .name {
    font-weight: 800; color: var(--navy); letter-spacing: -1px; line-height: 1;
  }

  .front-parent { left: 36px; top: 30px; font-size: 40px; }
  .front-agency { left: 325px; top: 26px; }
  .front-agency .mark { width: 56px; height: 56px; }
  .front-agency .name { font-size: 44px; }

  .emblem {
    position: absolute; left: 244px; top: 129px; width: 232px; height: 232px;
    border-radius: 50%; background: var(--navy);
  }

  .company-bar {
    position: absolute; left: 0; width: 100%; color: var(--white);
    font-size: 26px; font-weight: 600; display: flex; align-items: center;
    justify-content: center; padding-right: 40px;
  }
  .front-bar { top: 479px; height: 58px; }
  .back-bar { top: 467px; height: 59px; }

  .back-parent { right: 18px; top: 52px; font-size: 42px; }
  .back-agency { right: 14px; top: 104px; }
  .back-agency .mark { width: 54px; height: 54px; }
  .back-agency .name { font-size: 42px; }

  .person { position: absolute; left: 86px; top: 74px; }
  .person-name { font-size: 58px; line-height: 1; color: var(--ink); letter-spacing: 1px; }
  .person-name .first { font-weight: 800; }
  .person-name .last { font-weight: 300; }
  .person-role {
    margin-top: 12px; font-size: 15px; letter-spacing: 6.4px; color: var(--ink);
    text-transform: uppercase; font-weight: 400;
  }
  .person-role.tr { margin-top: 4px; color: var(--white); }

  .contact-list { position: absolute; left: 84px; top: 196px; list-style: none; }
  .contact-item { display: flex; align-items: center; gap: 12px; height: 46px; margin-bottom: 24px; }
  .contact-icon { width: 46px; height: 46px; flex: none; }
  .contact-text {
    font-size: 15px; font-weight: 600; color: var(--ink); line-height: 1.4;
    text-transform: uppercase;
  }
</style>
</head>
<body>
<main class="canvas">

  <section class="card card-front" aria-label="Card front">
    <svg class="card-shapes" viewBox="0 0 950 537" width="950" height="537" aria-hidden="true">
      <defs>
        <linearGradient id="frontBg" x1="0" y1="0" x2="1" y2="0">
          <stop offset="0" stop-color="#cdeef8"/>
          <stop offset="1" stop-color="#f4fbfe"/>
        </linearGradient>
        <linearGradient id="bandLight" x1="0" y1="0" x2="1" y2="0">
          <stop offset="0" stop-color="#8fd8ee"/>
          <stop offset="1" stop-color="#e7f7fc"/>
        </linearGradient>
        <linearGradient id="bandDark" x1="0" y1="0" x2="1" y2="0">
          <stop offset="0" stop-color="#3b7d99"/>
          <stop offset=".45" stop-color="#1f3f5c"/>
          <stop offset="1" stop-color="#172841"/>
        </linearGradient>
      </defs>
      <rect width="950" height="537" fill="url(#frontBg)"/>
      <path d="M822 0 H950 V537 H800 L598 268 Q586 250 598 232 Z" fill="url(#bandLight)"/>
      <path d="M950 89 V537 H820 L690 360 Q664 320 690 282 L740 230 Z" fill="url(#bandDark)"/>
      <path d="M0 479 H790 L832 537 H0 Z" fill="var(--navy)"/>
    </svg>

    <div class="brand-parent front-parent">TemaVista</div>
    <div class="brand-agency front-agency">
      <span class="mark"></span><span class="name">rahatrota</span>
    </div>
    <div class="emblem" aria-hidden="true"></div>
    <p class="company-bar front-bar">TemaVista Turizm ve Bilgi Teknolojileri A.Ş</p>
  </section>

  <section class="card card-back" aria-label="Card back">
    <svg class="card-shapes" viewBox="0 0 950 526" width="950" height="526" aria-hidden="true">
      <path d="M689 0 H950 V526 H904 L612 146 Q598 126 612 106 Z" fill="var(--white)"/>
      <path d="M0 467 H904 L950 526 H0 Z" fill="var(--navy)"/>
    </svg>

    <div class="brand-parent back-parent">TemaVista</div>
    <div class="brand-agency back-agency">
      <span class="mark"></span><span class="name">rahatrota</span>
    </div>

    <div class="person">
      <h1 class="person-name"><span class="first">ALEX</span><span class="last">MARLOW</span></h1>
      <p class="person-role">Marketing Director</p>
      <p class="person-role tr">Pazarlama Direktörü</p>
    </div>

    <ul class="contact-list">
      <li class="contact-item">
        <svg class="contact-icon" viewBox="0 0 46 46" aria-hidden="true">
          <circle cx="23" cy="23" r="21" fill="none" stroke="#fff" stroke-width="2"/>
          <path d="M12 24 L23 14 L34 24 H30 V33 H25.5 V27 H20.5 V33 H16 V24 Z" fill="#fff"/>
        </svg>
        <p class="contact-text">Harbor Lane 14<br>Moda District, Istanbul, Türkiye</p>
      </li>
      <li class="contact-item">
        <svg class="contact-icon" viewBox="0 0 46 46" aria-hidden="true">
          <circle cx="23" cy="23" r="21" fill="none" stroke="#fff" stroke-width="2"/>
          <path d="M16 13 Q13 14 13 18 Q15 28 28 33 Q32 33 33 30 L29 26 L26 28 Q20 25 18 20 L20 17 Z" fill="#fff"/>
        </svg>
        <p class="contact-text">+00 4321 8765 2109<br>+00 4321 8765 2109</p>
      </li>
      <li class="contact-item">
        <svg class="contact-icon" viewBox="0 0 46 46" aria-hidden="true">
          <circle cx="23" cy="23" r="21" fill="none" stroke="#fff" stroke-width="2"/>
          <rect x="13" y="16" width="20" height="14" rx="1.5" fill="#fff"/>
          <path d="M13.5 17 L23 24.5 L32.5 17" fill="none" stroke="var(--sky)" stroke-width="1.6"/>
        </svg>
        <p class="contact-text">info@rahatrota.com</p>
      </li>
    </ul>

    <p class="company-bar back-bar">TemaVista Turizm ve Bilgi Teknolojileri A.Ş</p>
  </section>

</main>
</body>
</html>
```